QRV (Guaranteed Project)

**Note: The girl image is not mandatory, that was just an idea, it may even look better with just text and no girl

TEXT (Lorne Bexley and Vantro logos large please):

PEOPLE GET READY (the font from the image below for people get ready looks good, kind of retro)

QRV WEEKEND 2014
SUNDAY MAY 25

430-9pm

QRV after party starts at 9pm-2am

Featuring
LORNE BEXLEY (SF) (use logo, largest name)
VANTRO (Sac) (use logo w/out the text below it, and slightly smaller than lorne bexley)

at K@Z Uptown 2847 J Street 21+

Project Deadline Extended
Reason: The mgr wants to review them and hasn't said yes yet.

Target Market(s)

House/Electronic Music Night Club

Font styles to use
Sans Serif

Colors
ec2027
ffffff

Requirements
Nice to have
• Would look nice with the red background and maybe a reddish filter on the girl

```html
<!DOCTYPE html>
<html lang="en">
<head>
<meta charset="utf-8">
<title>People Get Ready – QRV Weekend 2014</title>
<link href="https://fonts.googleapis.com/css2?family=Anton&family=Oswald:wght@300;400;500&display=swap" rel="stylesheet">
<style>
  :root {
    --red: #ec2027;
    --red-deep: #b5121a;
    --red-dark: #8e0c12;
    --white: #ffffff;
    --black: #050505;
    --haze: #c9c9c9;
  }
  html, body { margin: 0; padding: 0; overflow: hidden; background: var(--black); }
  .flyer {
    position: relative;
    width: 1200px;
    height: 940px;
    overflow: hidden;
    background: var(--black);
    color: var(--white);
  }
  .backdrop { position: absolute; inset: 0; }
  .headline, .date-block, .event-block, .venue, .lineup, .label-mark { position: absolute; }
  .display { font-family: "Anton", "Oswald", sans-serif; text-transform: uppercase; line-height: .86; }
  .headline { left: 34px; top: 14px; }
  .headline .line-1 { display: block; font-size: 232px; letter-spacing: -6px; }
  .headline .line-2 { display: block; font-size: 148px; letter-spacing: -4px; margin-top: 6px; }

  .date-block { right: 60px; top: 22px; width: 440px; }
  .date-block .day { display: block; font-size: 96px; letter-spacing: -2px; }
  .date-block .date { display: block; font-size: 146px; letter-spacing: -3px; text-align: right; margin-top: -4px; }
  .date-block .time { display: block; font-size: 104px; letter-spacing: -2px; text-align: right; margin-top: 4px; }
  .date-block .after { display: block; font-family: "Oswald", sans-serif; font-weight: 400; font-size: 26px; margin-top: 12px; text-align: right; }

  .event-block { right: 56px; top: 440px; text-align: right; }
  .event-block .title { display: block; font-size: 86px; letter-spacing: -1px; }
  .event-block .tagline { display: block; font-family: "Oswald", sans-serif; font-weight: 300; font-size: 50px; letter-spacing: 1px; margin-top: 14px; }

  .venue { right: 56px; top: 630px; text-align: right; font-family: "Oswald", sans-serif; font-weight: 300; }
  .venue .address { display: block; font-size: 40px; }
  .venue .age { display: block; font-size: 22px; margin-top: 10px; }

  .lineup { left: 36px; top: 798px; display: flex; align-items: center; gap: 56px; }
  .artist { font-family: "Oswald", sans-serif; font-weight: 400; color: var(--white); display: flex; align-items: center; gap: 14px; }
  .artist .dot { width: 70px; height: 70px; border-radius: 50%; background: var(--white); }
  .artist-lead .name { font-size: 52px; line-height: 1; text-transform: lowercase; }
  .artist-second .name { font-family: "Anton", sans-serif; font-size: 62px; letter-spacing: 4px; }

  .label-mark { right: 40px; top: 812px; display: flex; flex-direction: column; align-items: center; gap: 8px; }
  .label-mark .square { width: 56px; height: 56px; background: var(--red); }
  .label-mark .name { font-family: "Oswald", sans-serif; font-weight: 500; font-size: 14px; letter-spacing: 2px; }
</style>
</head>
<body>
<main class="flyer">
  <svg class="backdrop" width="1200" height="940" viewBox="0 0 1200 940" aria-hidden="false">
    <defs>
      <radialGradient id="stage-light" cx="0.25" cy="0.15" r="0.9">
        <stop offset="0" stop-color="#d8d8d8"/>
        <stop offset="0.35" stop-color="#8a8a8a"/>
        <stop offset="0.7" stop-color="#2a2a2a"/>
        <stop offset="1" stop-color="#050505"/>
      </radialGradient>
    </defs>
    <rect x="0" y="0" width="800" height="780" fill="url(#stage-light)" role="img" aria-label="Photo of a festival crowd with raised hands in front of stage lights"/>
    <rect x="0" y="780" width="1200" height="160" fill="var(--black)"/>
    <path d="M700 0 C440 240 300 560 520 940 H1200 V0 Z" fill="var(--red-dark)"/>
    <path d="M720 0 C480 250 350 560 590 940 H1200 V0 Z" fill="var(--red-deep)"/>
    <path d="M740 0 C520 260 410 560 660 940 H1200 V0 Z" fill="var(--red)"/>
    <path d="M760 0 C560 270 470 560 730 940 H1200 V0 Z" fill="var(--red-deep)" opacity="0.5"/>
    <path d="M780 0 C600 280 530 560 800 940 H1200 V0 Z" fill="var(--red)"/>
  </svg>

  <h1 class="headline display">
    <span class="line-1">People</span>
    <span class="line-2">Get Ready</span>
  </h1>

  <div class="date-block">
    <span class="day display">Sunday</span>
    <span class="date display">May 25</span>
    <span class="time display">4:30 9pm</span>
    <span class="after">QRV after party starts at 9pm-2am</span>
  </div>

  <div class="event-block">
    <span class="title display">QRV Weekend 2014</span>
    <span class="tagline">HOUSE MUSIC AT ITS FINEST</span>
  </div>

  <div class="venue">
    <span class="address">K@Z Uptown 2847 J Street</span>
    <span class="age">21+</span>
  </div>

  <div class="lineup">
    <div class="artist artist-lead"><span class="dot"></span><span class="name">lorne bexley</span></div>
    <div class="artist artist-second"><span class="name">VANTRO</span></div>
  </div>

  <div class="label-mark">
    <span class="square"></span>
    <span class="name">HALVERN MUSIC</span>
  </div>
</main>
</body>
</html>
```